Business Stationery - Business Cards - Letterheads, Compliment Slips

We need a new set of artwork designed for our client, they are a Construction Company, that also sell Kitchens, bathrooms and appliances.
They are an up and comping company that focus on quality and bespoke build. For them it is all about the quality of what they install, build or design. They have recently been awarded sole distributorship of a German kitchen brand Hannelore Moebel.
We need to present a quick job to them and provide some proofs for their new Artwork which encompasses all the elements of the company
The company name is the Tassel Group and we need to design a logo also.
Any Questions please let me know asap

Target Market(s)
Upmarket clients, or small Development companies.
Industry/Entity Type
Business
Look and feel
Each slider illustrates characteristics of the customer's brand and the style your logo design should communicate.

```html
<!DOCTYPE html>
<html lang="en">
<head>
<meta charset="utf-8">
<title>Tassel Group – Stationery Set</title>
<link rel="stylesheet" href="https://fonts.googleapis.com/css2?family=Montserrat:wght@500&family=EB+Garamond:wght@400&display=swap">
<style>
  :root {
    --backdrop: #e9eaea;
    --paper: #ffffff;
    --slate: #5b6e75;
    --slate-dark: #4c5e65;
    --accent: #5cc9a7;
    --ink: #3a3f42;
    --ink-soft: #6d7478;
    --rule: #d8dcdd;
  }
  * { box-sizing: border-box; margin: 0; padding: 0; }
  html, body { width: 1200px; height: 900px; overflow: hidden; }
  body {
    background: var(--backdrop);
    position: relative;
    font-family: "EB Garamond", Georgia, serif;
    color: var(--ink);
  }
  .sheet {
    position: absolute;
    background: var(--paper);
    box-shadow: 0 2px 6px rgba(0,0,0,.12);
  }
  .brand {
    font-family: "Montserrat", Arial, sans-serif;
    font-weight: 500;
    color: var(--accent);
    display: flex;
    align-items: center;
    gap: 6px;
    letter-spacing: .04em;
  }
  .brand__dot {
    width: 9px; height: 9px; border-radius: 50%;
    background: var(--accent);
  }

  /* Letterhead */
  .letterhead { left: 60px; top: 150px; width: 430px; height: 608px; padding: 40px 44px; }
  .letterhead .brand { font-size: 15px; }
  .letter { margin-top: 56px; font-size: 8.5px; line-height: 1.55; color: var(--ink-soft); }
  .letter p { margin-bottom: 9px; }
  .letter__sign { margin-top: 18px; }
  .letterhead__footer {
    position: absolute; left: 44px; bottom: 40px;
    font-size: 7px; line-height: 1.7; color: var(--ink-soft);
  }
  .letterhead__footer p + p { margin-top: 8px; }

  /* Compliment slip */
  .slip { left: 560px; top: 60px; width: 460px; height: 210px; padding: 30px 34px; }
  .slip .brand { font-size: 13px; }
  .slip__details {
    position: absolute; right: 40px; top: 50px;
    font-size: 7.5px; line-height: 1.7; color: var(--ink-soft);
  }
  .slip__details p + p { margin-top: 8px; }

  /* Envelope */
  .envelope {
    left: 560px; top: 300px; width: 460px; height: 230px;
    background: var(--slate);
  }
  .envelope svg { display: block; }

  /* Business cards */
  .card { top: 570px; width: 230px; height: 135px; }
  .card--back {
    left: 560px; background: var(--slate);
    display: flex; align-items: center; justify-content: center;
  }
  .card--back .brand { color: #ffffff; font-size: 13px; }
  .card--back .brand__dot { background: #ffffff; }
  .card--front { left: 820px; padding: 18px 16px; font-size: 7px; color: var(--ink-soft); }
  .card--front .brand { font-size: 9px; }
  .card__person { position: absolute; left: 16px; top: 44px; line-height: 1.5; }
  .card__name { font-size: 11px; color: var(--ink); }
  .card__contact { position: absolute; right: 16px; top: 20px; text-align: right; line-height: 1.6; }
  .card__contact p + p { margin-top: 7px; }

  .pencil {
    position: absolute; left: 1080px; top: 380px;
    width: 6px; height: 200px; background: #2f3234; border-radius: 2px;
  }
  .pencil::before {
    content: ""; position: absolute; top: -10px; left: 0;
    border-left: 3px solid transparent; border-right: 3px solid transparent;
    border-bottom: 10px solid #9a9d9f;
  }
</style>
</head>
<body>

  <article class="sheet letterhead">
    <div class="brand"><span class="brand__dot"></span>Tassel Group</div>
    <div class="letter">
      <p>Dear Ms Hale,</p>
      <p>Thank you for your recent enquiry about our bespoke kitchen and bathroom installations. We are pleased to share the proposal enclosed.</p>
      <p>Every project is planned with care, from the first survey to the final fitting, and built with materials chosen for lasting quality.</p>
      <p>Our team will visit your site next week to confirm measurements and discuss finishes, appliances and the schedule of works.</p>
      <p>Please contact us with any questions.</p>
      <p class="letter__sign">Best Regards,<br>Ms Clara Hale</p>
    </div>
    <footer class="letterhead__footer">
      <p>office@tasselgroup.co<br>00 5550 123 456</p>
      <p>Harbour Lane 12<br>Riverton</p>
    </footer>
  </article>

  <article class="sheet slip">
    <div class="brand"><span class="brand__dot"></span>Tassel Group</div>
    <div class="slip__details">
      <p>With compliments</p>
      <p>Harbour Lane 12<br>Riverton</p>
      <p>00 5550 123 456<br>office@tasselgroup.co</p>
    </div>
  </article>

  <div class="sheet envelope">
    <svg width="460" height="230" viewBox="0 0 460 230" aria-hidden="true">
      <polygon points="0,0 460,0 230,90" fill="var(--slate-dark)" opacity=".35"/>
    </svg>
  </div>

  <div class="sheet card card--back">
    <div class="brand"><span class="brand__dot"></span>Tassel Group</div>
  </div>

  <div class="sheet card card--front">
    <div class="brand"><span class="brand__dot"></span>Tassel Group</div>
    <div class="card__person">
      <div class="card__name">Aldous Penrith</div>
      <div>Project Manager</div>
    </div>
    <div class="card__contact">
      <p>Harbour Lane 12<br>Riverton</p>
      <p>00 5550 123 456</p>
      <p>office@tasselgroup.co<br>www.tasselgroup.co</p>
    </div>
  </div>

  <div class="pencil" aria-hidden="true"></div>

</body>
</html>
```